Outdoor sign for Brindle Auto Restoration

I need a horizontal 4'x 8' outdoor roadside sign for my classic auto restoration business. I have uploaded colors and our logo. Needs the Brindle name, a prominent Classic AUTO RESTORATION, phone number and website. We rebuild and restore vintage cars, trucks and 4x4s. I'd like something clean but possibly retro. Classic Auto Restoration is more important than the Brindle name. It needs to be visible and readable from the street. NO CLIP ART

Target Market(s)

Customers who need their vintage care restored or upgraded. Men and women ages 25-75

Industry/Entity Type

Automotive

Colors
FFC000
F8CF3A
FAE287
FDF2CF
FEFAEE

Requirements
Must have
• Legible. Bright. Readable as a backlit 4' x 8' large horizontal sign (roughly 120cm X 240cm)
Nice to have
• Use of the Brindle logo/type, Complete or Classic before prominent AUTO RESTORATION
Should not have
• Clip art of old cars or icons. And we don't want the Brindle Logo from the website because it wont be legible from the road. I have included the Illustrator file for Brindle text in the uploads

```html
<!DOCTYPE html>
<html lang="en">
<head>
<meta charset="utf-8">
<title>Brindle Auto Restoration – Roadside Sign</title>
<link rel="stylesheet" href="https://fonts.googleapis.com/css2?family=Ultra&family=Anton&family=Roboto+Condensed:wght@700&display=swap">
<style>
  :root {
    --backdrop: #6d6e71;
    --sign-white: #ffffff;
    --sign-black: #1a1a1a;
    --sign-yellow: #f6b01c;
    --checker-tint: #fbd77a;
  }
  html, body {
    margin: 0;
    padding: 0;
    width: 1200px;
    height: 681px;
    overflow: hidden;
    background: var(--backdrop);
  }
  .roadside-sign {
    position: absolute;
    left: 80px;
    top: 82px;
    width: 1038px;
    height: 518px;
    display: block;
  }
  .band-white { fill: var(--sign-white); }
  .band-black { fill: var(--sign-black); }
  .band-yellow { fill: var(--sign-yellow); }
  .checker-strip { fill: var(--checker-tint); }
  .headline {
    font-family: "Ultra", "Rockwell", serif;
  }
  .headline-classic { fill: var(--sign-black); font-size: 124px; }
  .headline-auto { fill: var(--sign-yellow); font-size: 124px; }
  .headline-restoration { fill: var(--sign-white); font-size: 138px; }
  .tagline {
    font-family: "Roboto Condensed", "Arial Narrow", sans-serif;
    font-weight: 700;
    font-size: 54px;
    fill: var(--sign-black);
  }
  .brand-name {
    font-family: "Anton", "Impact", sans-serif;
    font-size: 118px;
    fill: var(--sign-white);
  }
  .phone {
    font-family: "Roboto Condensed", "Arial Narrow", sans-serif;
    font-weight: 700;
    font-size: 72px;
    fill: var(--sign-white);
  }
  .website {
    font-family: "Roboto Condensed", "Arial Narrow", sans-serif;
    font-weight: 700;
    font-size: 38px;
    fill: var(--sign-black);
  }
</style>
</head>
<body>
  <svg class="roadside-sign" viewBox="0 0 1038 518" xmlns="http://www.w3.org/2000/svg" aria-label="Brindle Auto Restoration roadside sign">
    <rect class="band-white" x="0" y="0" width="1038" height="121"/>
    <rect class="band-black" x="0" y="121" width="1038" height="126"/>
    <rect class="checker-strip" x="0" y="247" width="1038" height="24" role="img" aria-label="Checkered flag strip in white and yellow"/>
    <rect class="band-yellow" x="0" y="271" width="1038" height="247"/>

    <text class="headline" x="23" y="101" textLength="995" lengthAdjust="spacingAndGlyphs"><tspan class="headline-classic">CLASSIC </tspan><tspan class="headline-auto">AUTO</tspan></text>
    <text class="headline headline-restoration" x="25" y="231" textLength="980" lengthAdjust="spacingAndGlyphs">RESTORATION</text>

    <text class="tagline" x="32" y="354" textLength="973" lengthAdjust="spacingAndGlyphs">Restoring Vintage Cars, Trucks &amp; 4x4s</text>

    <text class="brand-name" x="32" y="488" textLength="540" lengthAdjust="spacingAndGlyphs">BRINDLE</text>

    <text class="phone" x="635" y="447" textLength="370" lengthAdjust="spacingAndGlyphs">501-555-0142</text>
    <text class="website" x="635" y="486" textLength="368" lengthAdjust="spacingAndGlyphs">brindle autoworks.com</text>
  </svg>
</body>
</html>
```